Label - Australian Extra Virgin Olive Oil

I'm seeking a front and back label to apply to bottles/tins of my olive oil. They will be applied to green bottles of various sizes and also white tins. The labels will have the dimensions 70 x 120mm and printed at 600dpi on adhesive labels with metalised backing. With this material, any area which is not colored on the label will show through as silver - the design may make use of this feature. There are some obligatory labeling requirements in Australia including a logo showing the proportion of Australian content, and an indication of the harvest date - the design will need to make allowance for this. Also, since the label will be used in subsequent years and on various sizes of product, I need to be able to alter this with each print run.I have a logo to use on the front label and another I would like to use on the back as this latter one will tie in with other future products (non olive oil).
The text for the back label
"Tallowby Creek is a family run enterprise. Our olives are grown on the banks of the Wendrake River in Central Victoria and processed locally
email; quietheron@pelinet.com.au
text needed for the front label design
"Australian Extra-Virgin Olive Oil"

```html
<!DOCTYPE html>
<html lang="en">
<head>
<meta charset="utf-8">
<title>Tallowby Creek – Olive Oil Labels</title>
<link rel="stylesheet" href="https://fonts.googleapis.com/css2?family=Marcellus+SC&display=swap">
<style>
  :root {
    --backdrop-top: #4a4a4a;
    --backdrop-bottom: #1e1e1e;
    --silver-dark: #8e8e8e;
    --silver-mid: #cdcdcd;
    --silver-light: #f6f6f6;
    --ink: #111111;
    --ornament-tone: #5a5a5a;
    --leaf-tone: #3c3c3c;
    --badge-tone: #1a1a1a;
  }
  * { box-sizing: border-box; margin: 0; padding: 0; }
  html, body { width: 1200px; height: 1200px; overflow: hidden; }
  body {
    background: linear-gradient(180deg, var(--backdrop-top), var(--backdrop-bottom));
    font-family: "Marcellus SC", serif;
    color: var(--ink);
    position: relative;
  }
  .label {
    position: absolute;
    top: 257px;
    width: 400px;
    height: 686px;
    background: linear-gradient(135deg, var(--silver-dark) 0%, var(--silver-light) 35%, var(--silver-mid) 55%, var(--silver-light) 78%, var(--silver-dark) 100%);
  }
  .label--back { left: 150px; }
  .label--front { left: 650px; }
  .label__frame {
    position: absolute;
    inset: 14px;
    border: 2px solid var(--ink);
  }
  .label__ornament {
    position: absolute;
    width: 110px;
    height: 110px;
    background: radial-gradient(circle at 50% 50%, var(--ornament-tone), transparent 70%);
    opacity: 0.55;
  }
  .ornament--top-left { top: 6px; left: 6px; }
  .ornament--top-right { top: 6px; right: 6px; }
  .ornament--bottom-left { bottom: 6px; left: 6px; }
  .ornament--bottom-right { bottom: 6px; right: 6px; }

  .back__title {
    position: absolute;
    top: 72px; left: 0; right: 0;
    text-align: center;
    font-size: 30px;
    letter-spacing: 1px;
  }
  .back__story {
    position: absolute;
    top: 118px; left: 50px; right: 50px;
    font-size: 17px;
    line-height: 1.28;
    text-align: justify;
  }
  .back__care {
    position: absolute;
    top: 420px; left: 50px; right: 50px;
    font-size: 17px;
    line-height: 1.25;
    font-weight: 700;
  }

  .front__title {
    position: absolute;
    top: 150px; left: 0; right: 0;
    text-align: center;
    font-size: 40px;
    letter-spacing: 1px;
  }
  .front__illustration {
    position: absolute;
    top: 215px; left: 135px;
    width: 130px; height: 100px;
    border-radius: 50%;
    background: radial-gradient(ellipse at 50% 50%, var(--leaf-tone), transparent 72%);
  }
  .front__product {
    position: absolute;
    top: 340px; left: 0; right: 0;
    text-align: center;
    font-size: 38px;
    line-height: 1.15;
  }
  .front__origin-badge {
    position: absolute;
    right: 42px; bottom: 62px;
    width: 52px; height: 72px;
    background: var(--badge-tone);
  }
</style>
</head>
<body>
  <section class="label label--back" aria-label="Back label">
    <div class="label__frame"></div>
    <div class="label__ornament ornament--top-left" role="img" aria-label="Decorative scroll flourish in the corner"></div>
    <div class="label__ornament ornament--bottom-right" role="img" aria-label="Decorative scroll flourish in the corner"></div>
    <h2 class="back__title">Tallowby Creek</h2>
    <p class="back__story">Our grove sits on a gentle slope beside quiet water, where warm days and cool nights bring slow, even ripening. Each fruit is picked by hand at its peak, pressed within hours and bottled close to home, so the oil keeps its fresh green taste and a soft peppery finish on the tongue.</p>
    <p class="back__care">Store away from light and heat. Best used within a year of harvest.</p>
  </section>

  <section class="label label--front" aria-label="Front label">
    <div class="label__frame"></div>
    <div class="label__ornament ornament--top-right" role="img" aria-label="Decorative scroll flourish in the corner"></div>
    <div class="label__ornament ornament--bottom-left" role="img" aria-label="Decorative scroll flourish in the corner"></div>
    <h1 class="front__title">Tallowby Creek</h1>
    <div class="front__illustration" role="img" aria-label="Illustration of an olive sprig with leaves and fruit"></div>
    <p class="front__product">Australian<br>Extra-Virgin<br>Olive Oil</p>
    <div class="front__origin-badge" role="img" aria-label="Country of origin badge"></div>
  </section>
</body>
</html>
```